TERRAVOL " need somthing eye catching and envirnmental friendely materials

Business Card " UNIQUE..
- use the agreed on logo.
- use wooden background.
- the environmental sound should be HIGH.

Company slogan is ZERO DISCHARGE.
We work in deploying the latest technology “ USA & Europe” in the field of drill cutting recycle and economically managing the footprint.
With the ramp up in oil demands and the increase in oil prices , operators are extending their operations into new geographical areas “ government regulations and eco-sounds” created the need to a specialty services and products that should go parallel or even ahead.

Target Market(s)

OIL field and environmental concerned.
Mainly ENGINEERS.

Industry/Entity Type

Government

Font styles to use
Decorative
Script

Colors

Designer to choose colors to be used in the design.

Requirements
Must have
• Eco - sounded.

```html
<!DOCTYPE html>
<html lang="en">
<head>
<meta charset="utf-8">
<title>TERRAVOL Business Card</title>
<link rel="stylesheet" href="https://fonts.googleapis.com/css2?family=Tinos:wght@400;700&display=swap">
<style>
  :root {
    --backdrop: #a9aeae;
    --wood-dark: #5e4423;
    --wood-mid: #7d5f33;
    --wood-light: #9a7a47;
    --eco-green: #5cc41c;
    --ink: #2a1d0c;
  }
  html, body {
    margin: 0;
    padding: 0;
    width: 1200px;
    height: 1000px;
    overflow: hidden;
    background: var(--backdrop);
    font-family: "Tinos", "Times New Roman", serif;
  }
  .canvas {
    position: relative;
    width: 1200px;
    height: 1000px;
  }
  .card {
    position: absolute;
    border-radius: 22px;
    overflow: hidden;
  }
  .card--front { left: 28px; top: 24px; width: 732px; height: 466px; }
  .card--back  { left: 442px; top: 508px; width: 730px; height: 467px; }
  .wood-surface {
    position: absolute;
    inset: 0;
    background: linear-gradient(115deg, var(--wood-dark) 0%, var(--wood-mid) 35%, var(--wood-light) 55%, var(--wood-mid) 75%, var(--wood-dark) 100%);
  }
  .content { position: absolute; inset: 0; }
  .brand {
    position: absolute;
    display: flex;
    align-items: center;
    gap: 14px;
    color: var(--eco-green);
    font-weight: 700;
    letter-spacing: 2px;
  }
  .brand__dot {
    border-radius: 50%;
    background: var(--eco-green);
  }
  .brand--front { left: 60px; top: 200px; font-size: 50px; }
  .brand--front .brand__dot { width: 40px; height: 40px; }
  .brand--back { left: 22px; top: 95px; font-size: 30px; }
  .brand--back .brand__dot { width: 24px; height: 24px; }
  .slogan {
    position: absolute;
    margin: 0;
    color: var(--eco-green);
    font-weight: 400;
    line-height: 0.95;
  }
  .slogan--front { left: 459px; top: 160px; font-size: 64px; }
  .slogan--back { left: 246px; top: 28px; font-size: 64px; white-space: nowrap; }
  .holder {
    position: absolute;
    left: 8px;
    top: 296px;
    color: var(--ink);
  }
  .holder__name { margin: 0; font-size: 27px; letter-spacing: 1px; line-height: 1.05; }
  .holder__title { margin: 0; font-size: 23px; font-weight: 700; line-height: 1.05; }
  .contact {
    position: absolute;
    left: 8px;
    top: 390px;
    margin: 0;
    padding: 0;
    list-style: none;
    color: var(--ink);
    font-size: 20px;
    font-weight: 700;
    line-height: 0.98;
  }
</style>
</head>
<body>
<main class="canvas">
  <section class="card card--front">
    <div class="wood-surface" role="img" aria-label="Weathered wooden plank texture"></div>
    <div class="content">
      <div class="brand brand--front"><span class="brand__dot"></span>TERRAVOL</div>
      <h1 class="slogan slogan--front">Zero<br>Discharge</h1>
    </div>
  </section>

  <section class="card card--back">
    <div class="wood-surface" role="img" aria-label="Weathered wooden plank texture"></div>
    <div class="content">
      <div class="brand brand--back"><span class="brand__dot"></span>TERRAVOL</div>
      <h2 class="slogan slogan--back">Zero Discharge</h2>
      <div class="holder">
        <p class="holder__name">KARIM NABIL SAEED</p>
        <p class="holder__title">Chief Executive Officer</p>
      </div>
      <ul class="contact">
        <li>Phone : 009715 555 010 42</li>
        <li>Mail : IT@TERRAVOL.com</li>
        <li>Web : www.TERRAVOL.ae</li>
      </ul>
    </div>
  </section>
</main>
</body>
</html>
```